Corporate Branding - Web and Print

A UK based company will like to use an existing logo to create branding materials for all marketing related documents, including business card, prints, letterhead, Website, Twitter, Facebook, Instagram logo etc. This company serves high-end clientele in the fashion, health and wellness and as such high quality and class is of utmost importance.
Where the logo can be modernised without losing its character then experiment. The main thing is to have a corporate branding which can be used later for brochures, Business Plan infographics.
The prominent colour within the organisation is burnt orange with no secondary colour. However if you believe a secondary colour is needed then use it, otherwise keep it simple and classy. Any chosen colours have to match perfectly.
Target Market(s)
High net worth individuals
Industry/Entity Type
Health And Wellness
Contact Information for Business Card
classy

```html
<!DOCTYPE html>
<html lang="en">
<head>
<meta charset="utf-8">
<title>Velmora — Business Card</title>
<link href="https://fonts.googleapis.com/css2?family=Roboto:wght@400;500;700;900&display=swap" rel="stylesheet">
<style>
  :root {
    --burnt-orange: #ee8d1c;
    --burnt-orange-light: #f2a03a;
    --card-white: #f7f7f5;
    --ink: #3a3a3a;
    --backdrop: #2a2a2a;
  }
  * { margin: 0; padding: 0; box-sizing: border-box; }
  html, body {
    width: 1200px; height: 886px; overflow: hidden;
    background: var(--backdrop);
    font-family: "Roboto", Arial, sans-serif;
  }
  .stage {
    width: 1200px; height: 886px;
    display: flex; align-items: center; justify-content: center; gap: 80px;
  }
  .card {
    width: 430px; height: 730px;
    border-radius: 34px;
    position: relative;
    overflow: hidden;
  }
  /* front */
  .card--front {
    background: linear-gradient(160deg, var(--burnt-orange-light), var(--burnt-orange) 55%);
    color: #fff;
  }
  .front-brand {
    position: absolute; left: 0; right: 0; top: 300px;
    display: flex; flex-direction: column; align-items: center; gap: 22px;
  }
  .brand-dot {
    width: 96px; height: 96px; border-radius: 50%; background: #fff;
  }
  .front-brand .brand-name {
    font-weight: 900; font-size: 44px; letter-spacing: 4px; color: #fff;
  }
  .front-url {
    position: absolute; left: 0; right: 0; bottom: 48px;
    text-align: center; font-size: 15px; letter-spacing: 6px; font-weight: 400;
  }
  /* back */
  .card--back { background: var(--card-white); }
  .back-brand {
    position: absolute; left: 52px; top: 70px;
    display: flex; align-items: center; gap: 16px;
  }
  .back-brand .brand-dot {
    width: 54px; height: 54px; background: var(--burnt-orange);
  }
  .back-brand .brand-name {
    font-weight: 900; font-size: 50px; letter-spacing: 3px; color: var(--burnt-orange);
  }
  .contact {
    position: absolute; left: 150px; top: 330px;
    color: var(--ink); font-size: 17px; line-height: 1.45;
  }
  .contact-name {
    color: var(--burnt-orange); font-weight: 500; font-size: 22px; text-transform: uppercase;
  }
  .contact-role {
    font-weight: 500; font-size: 19px; text-transform: uppercase; margin-bottom: 18px;
  }
  .contact-address { margin-bottom: 18px; }
  .contact-lines { list-style: none; }
  .contact-lines .label { color: var(--burnt-orange); font-weight: 700; margin-right: 6px; }
</style>
</head>
<body>
<main class="stage">
  <section class="card card--front" aria-label="Card front">
    <div class="front-brand">
      <span class="brand-dot"></span>
      <span class="brand-name">VELMORA</span>
    </div>
    <p class="front-url">www.velmora.com</p>
  </section>

  <section class="card card--back" aria-label="Card back">
    <div class="back-brand">
      <span class="brand-dot"></span>
      <span class="brand-name">VELMORA</span>
    </div>
    <div class="contact">
      <p class="contact-name">Daniel Hart</p>
      <p class="contact-role">CEO/Founder</p>
      <p class="contact-address">2140 Linden Court<br>Bristol, Avon BS1 4QA</p>
      <ul class="contact-lines">
        <li><span class="label">P:</span>614 208 7731</li>
        <li><span class="label">M:</span>752 319 4086</li>
        <li><span class="label">F:</span>530 674 2219</li>
        <li><span class="label">E:</span>daniel@velmora.com</li>
        <li><span class="label">W:</span>www.velmora.com</li>
      </ul>
    </div>
  </section>
</main>
</body>
</html>
```